Pale Meadow Distillery
Exceptional Handcrafted Spirits
Designers, I want to personally thank all of you for your help and support on Pale Meadow Distillery. It was a close tie amongst many of you. In the end I had a very difficult time choosing a winner. Please keep up the good work and look for my next project to start later next week. You guys are awesome!!!
All, please let me know what other files I can get you so that the word "distillery" appears correct. Some of you are having to remove the word from the barrels and it leaves a blank spot. I can try and get you any of the original corel draw (cdr) files from the logo designer.
The two fonts used in my logo are Goudy Old Style and PassionConflictROB.
All designers, I am looking for a one side business card.
could you please upload ai or eps file of logo

```html
<!DOCTYPE html>
<html lang="en">
<head>
<meta charset="utf-8">
<title>Pale Meadow Distillery – Stationery</title>
<link rel="stylesheet" href="https://fonts.googleapis.com/css2?family=Sorts+Mill+Goudy&display=swap">
<style>
  :root{
    --bg:#e9e6e1;
    --paper:#ffffff;
    --ink:#1a1a1a;
    --ink-soft:#555555;
    --brand-red:#c8102e;
    --black-card:#121212;
    --faint:#ececec;
  }
  *{box-sizing:border-box;margin:0;padding:0}
  html,body{width:1200px;height:701px;overflow:hidden;background:var(--bg)}
  body{position:relative;font-family:"Sorts Mill Goudy",Georgia,serif;color:var(--ink)}
  .piece{position:absolute;background:var(--paper);box-shadow:0 2px 6px rgba(0,0,0,.25);overflow:hidden}
  .wordmark{display:flex;align-items:center;gap:5px;font-size:13px;letter-spacing:.5px;text-transform:uppercase;white-space:nowrap;color:var(--ink)}
  .wordmark .dot{width:9px;height:9px;border-radius:50%;background:currentColor;flex:none}
  .wordmark.small{font-size:10px;gap:4px}
  .wordmark.small .dot{width:7px;height:7px}
  .line{font-size:5.5px;color:var(--ink-soft);white-space:nowrap;letter-spacing:.2px}
  .faint-mark{position:absolute;border-radius:50%;background:var(--faint)}

  .letterhead{top:65px;width:288px;height:523px}
  .letterhead.one{left:53px}
  .letterhead.two{left:365px}
  .letterhead .wordmark{position:absolute;top:22px;left:18px}
  .letterhead .line.address{position:absolute;top:42px;left:18px}
  .letterhead.one .footer{position:absolute;bottom:22px;left:0;right:0;text-align:center}
  .letterhead.two .wordmark{left:50%;transform:translateX(-50%)}
  .letterhead.two .footer{position:absolute;bottom:22px;left:50%;transform:translateX(-50%);text-align:center}
  .letterhead .faint-mark{width:90px;height:90px;left:99px;bottom:50px}

  .card{width:200px;height:125px;top:65px;text-align:center}
  .card.black{left:677px;background:var(--black-card)}
  .card.black .wordmark{color:#fff;position:absolute;top:18px;left:50%;transform:translateX(-50%)}
  .card.black .info{position:absolute;bottom:22px;left:0;right:0}
  .card.black .line{color:#cfcfcf}
  .card.white{left:898px;width:197px}
  .card.white .wordmark{position:absolute;top:14px;left:50%;transform:translateX(-50%)}
  .card .name{position:absolute;top:56px;left:0;right:0;font-size:9px;color:var(--brand-red)}
  .card .role{position:absolute;top:69px;left:0;right:0}
  .card.white .info{position:absolute;bottom:14px;left:0;right:0}
  .card.red{left:773px;top:202px;width:192px;height:115px;background:var(--brand-red)}
  .card.red .tagline{position:absolute;top:64px;left:0;right:0;font-size:6.5px;color:#fff;letter-spacing:.6px}

  .envelope{left:677px;width:418px;height:127px}
  .envelope.front-a{top:360px}
  .envelope.front-b{top:504px}
  .envelope .wordmark{position:absolute;top:14px;left:16px}
  .envelope .sender{position:absolute;top:34px;left:16px;line-height:8px}
  .envelope .faint-mark{width:70px;height:70px;right:38px;top:34px}

  .envelope-back{left:235px;top:528px;width:293px;height:132px}
  .envelope-back svg{position:absolute;inset:0}
</style>
</head>
<body>

  <!-- Letterhead, left aligned -->
  <section class="piece letterhead one">
    <div class="wordmark"><span class="dot"></span>Pale Meadow Distillery</div>
    <p class="line address">410 Willow Lane · Brookfield, VT 05036</p>
    <div class="faint-mark"></div>
    <div class="footer">
      <p class="line">Phone: 802-555-0142 · Fax: 802-555-0143 · www.palemeadow.com</p>
      <p class="line">info@palemeadow.com · Mast42</p>
    </div>
  </section>

  <!-- Letterhead, centered -->
  <section class="piece letterhead two">
    <div class="wordmark"><span class="dot"></span>Pale Meadow Distillery</div>
    <div class="faint-mark"></div>
    <div class="footer">
      <p class="line">410 Willow Lane · Brookfield, VT 05036</p>
      <p class="line">Phone: 802-555-0142 · Fax: 802-555-0143</p>
      <p class="line">info@palemeadow.com · www.palemeadow.com</p>
    </div>
  </section>

  <!-- Business cards -->
  <section class="piece card black">
    <div class="wordmark small"><span class="dot"></span>Pale Meadow Distillery</div>
    <div class="info">
      <p class="line">410 Willow Lane · Brookfield, VT 05036</p>
      <p class="line">Phone: 802-555-0142 · Fax: 802-555-0143</p>
      <p class="line">www.palemeadow.com</p>
    </div>
  </section>

  <section class="piece card white">
    <div class="wordmark small"><span class="dot"></span>Pale Meadow Distillery</div>
    <p class="name">Karl Brusby</p>
    <p class="line role">Master Distiller</p>
    <div class="info">
      <p class="line">410 Willow Lane · Brookfield, VT 05036</p>
      <p class="line">Phone: 802-555-0142 · karl@palemeadow.com</p>
    </div>
  </section>

  <section class="piece card red">
    <p class="tagline">Exceptional Handcrafted Spirits</p>
  </section>

  <!-- Envelopes, front -->
  <section class="piece envelope front-a">
    <div class="wordmark small"><span class="dot"></span>Pale Meadow Distillery</div>
    <div class="sender">
      <p class="line">410 Willow Lane</p>
      <p class="line">Brookfield, VT 05036</p>
    </div>
    <div class="faint-mark"></div>
  </section>

  <section class="piece envelope front-b">
    <div class="wordmark small"><span class="dot"></span>Pale Meadow Distillery</div>
    <div class="sender">
      <p class="line">410 Willow Lane</p>
      <p class="line">Brookfield, VT 05036</p>
    </div>
  </section>

  <!-- Envelope, back with flap -->
  <section class="piece envelope-back">
    <svg width="293" height="132" viewBox="0 0 293 132">
      <path d="M0 0 H293 V18 L160 52 Q146.5 56 133 52 L0 18 Z" fill="var(--black-card)"/>
      <circle cx="146.5" cy="44" r="13" fill="var(--paper)" stroke="var(--black-card)" stroke-width="2"/>
    </svg>
  </section>

</body>
</html>
```